Business Card Design Project

We have a logo design and are now looking for a business card design. We supply pre-construction services to the Wireless Telecommunication Industry in the development of cell phone tower and other antenna supporting infrastructure e.g. buildings. The types of services include Real Estate Leasing, Zoning & Permitting,Surveying and A&E work. I am looking for a card that includes the logo we have selected along with the full company name. Company colors are Blue and Silver. I want something professional and that "pops". Use your imagination with the four sided star portion of the logo - it can be stretched such that it occupies a large portion of the card or kept simple the way it is. I am interested in seeing the design on a white, silver, navy, black or charcoal background or any other color you think works well with the logo. Apart from the logo that includes HRM we also need to see the full company name on the card - Harborline Relay Maintenance, Inc. The design must also show a persons name, title, address, (2) phone numbers, e-mail address and web address www.hrm.example

Target Market(s)

Cell phone carriers e.g. Quellport Mobile, BN&K, Zandex Cell, Ovalo etc.

Industry/Entity Type

Cell Phone

Requirements
Must have
• Logo and
Harborline Relay Maintenance, Inc.

```html
<!DOCTYPE html>
<html lang="en">
<head>
<meta charset="utf-8">
<title>Harborline Relay Maintenance, Inc. — Business Card</title>
<link rel="stylesheet" href="https://fonts.googleapis.com/css2?family=Arimo:wght@400;700&display=swap">
<style>
  :root {
    --backdrop: #e4e6e8;
    --card: #ffffff;
    --blue: #2a9ee0;
    --blue-light: #6cc4f2;
    --blue-deep: #1679c4;
    --ink: #2b2b2b;
    --label: #4a4a4a;
    --value: #8c8c8c;
  }
  * { box-sizing: border-box; margin: 0; padding: 0; }
  html, body {
    width: 1200px;
    height: 900px;
    overflow: hidden;
    background: var(--backdrop);
    font-family: "Arimo", Arial, sans-serif;
  }
  .sheet {
    position: relative;
    width: 1200px;
    height: 900px;
  }
  .card {
    position: absolute;
    left: 320px;
    width: 560px;
    height: 320px;
    background: var(--card);
    overflow: hidden;
    box-shadow: 0 10px 30px rgba(0,0,0,0.12), 0 2px 6px rgba(0,0,0,0.08);
  }
  .card--front { top: 100px; }
  .card--back { top: 480px; }

  /* Front */
  .front-disc {
    position: absolute;
    left: -150px;
    top: -30px;
    width: 380px;
    height: 380px;
    border-radius: 50%;
    background: radial-gradient(circle at 62% 48%, var(--blue-light) 0%, var(--blue) 45%, var(--blue-deep) 100%);
  }
  .front-name {
    position: absolute;
    right: 36px;
    bottom: 40px;
    width: 240px;
    text-align: right;
    color: var(--ink);
    font-weight: 400;
    font-size: 22px;
    line-height: 1.25;
  }

  /* Back */
  .back-mark {
    position: absolute;
    left: 52px;
    top: 136px;
    display: flex;
    align-items: center;
    gap: 12px;
  }
  .back-mark__dot {
    width: 26px;
    height: 26px;
    border-radius: 50%;
    background: var(--blue);
  }
  .back-mark__name {
    color: var(--blue);
    font-weight: 400;
    font-size: 40px;
    line-height: 1;
  }
  .contact {
    position: absolute;
    left: 268px;
    top: 48px;
    color: var(--value);
  }
  .contact__name {
    color: var(--label);
    font-size: 28px;
    line-height: 1;
  }
  .contact__title {
    font-size: 10px;
    margin-top: 2px;
    margin-bottom: 20px;
  }
  .contact__row {
    display: flex;
    gap: 10px;
    font-size: 18px;
    line-height: 22px;
    margin-bottom: 14px;
  }
  .contact__label { color: var(--label); }
  .contact__value { color: var(--value); }
</style>
</head>
<body>
  <main class="sheet">
    <section class="card card--front" aria-label="Card front">
      <div class="front-disc" aria-hidden="true"></div>
      <p class="front-name">Harborline Relay Maintenance, Inc.</p>
    </section>

    <section class="card card--back" aria-label="Card back">
      <div class="back-mark">
        <span class="back-mark__dot" aria-hidden="true"></span>
        <span class="back-mark__name">HRM</span>
      </div>
      <div class="contact">
        <p class="contact__name">Name</p>
        <p class="contact__title">title</p>
        <div class="contact__row">
          <span class="contact__label">phone</span>
          <span class="contact__value">(415) 555 - 018<br>(415) 555 - 027</span>
        </div>
        <div class="contact__row">
          <span class="contact__label">address</span>
          <span class="contact__value">48 Pier Road</span>
        </div>
        <div class="contact__row">
          <span class="contact__label">email</span>
          <span class="contact__value">name@hrm.example</span>
        </div>
        <div class="contact__row">
          <span class="contact__label">web</span>
          <span class="contact__value">www.hrm.example</span>
        </div>
      </div>
    </section>
  </main>
</body>
</html>
```